Brisa Nord Premium Cooling Towel

Similar to Zeph Ox, Valtane and Murex. Brisa Nord's Products are a premium brand within the cooling market. From towels to high performance sports products Brisa nords products crush the competitors. The product regardless of the conditions stays cold even in the hottest conditions. Our current clients range from the Tall Pines, Hovard Lane's to professional athletes. We are currently redesigning our packaging for our towel line.

The goal of this design is to have someone look at the package and say "Whoa...". When customers first try the product they have a good idea of what to expect, then they try it and are blown away. Simply put the towel sells itself. Sales reps have stated that the highest closing rates are when they say nothing at all.

With that being said we are looking for a packaging that has the same effect. Imagine you are sitting by the pool side in Miami in the middle of the summer, you feel like your body is on fire. Someone then offers you a brisa nord towel that instantly cools you making the unbearable suddenly... enjoyable.

Yes, this is the effect we are looking for off the shelf. If this were on the shelf at Shopwell in the container how do we get this same effect. Things that our customers have indicated were a plus was when the cooling effect was displayed by both color and transition of the logo. This effect typically takes some layering in photo shop but when done right results in a much higher customer rating.

The containers are a plastic tube (roughly 10 inch by 3 inch in by diameter) and an envelope style pouch that is 10inch by 6inch. Official dimensions will be updated later this week.

We are looking for a simple clean look that screams "premium". Again, the "whoa" factor is a must to stand out against competitors. The main color schemes to consider are hot red, Ice cold blue, silver, black. Realizing that building a a compelling design that relates to an audience of 16-30 Male and Female is tough please ask questions. It must connect to parents, teens and active athletes. Again, think Zeph Ox and how it connects with everyone.

Competitors:
1. http://www.example-toolyard.com/brisk-wrap-sport-cooling-towel.html

2.http://www.example-rangedeals.net/product/0-0000000

3. http://www.example-bazaarhub.com/Vantor-Frostline-Instant-Cooling-Towel/dp/X000000000

4. http://www.example-glacierwraps.com/

5. http://www.example-trailmark.com/Dura-Frost-Cooling-Performance-Clothing-Apparel/Technology_Dura-Frost.html

6. http://www.example-lookfind.com/shopping/ridgeline-outfitters-team-cooling-towel-white-0000000/p/X000000000

7. http://www.example-marigoldmail.com/p/Floe-Rest-Towel-Blue.cfm?tid=000000000

8.https://www.example-breezecloths.com/

9. http://www.example-pricepeek.com/cooling-towels/products-html#!

Reason: Due to a massive influx of designs we will be extending the project for four additional days to fairly evaluate all of the designs. No new designs will be considered after today (April 19th). I will be sending out the designs to our network and the one that gets the most votes wins. I really appreciate all of the different designs and will keep you posted on the vote count.

16-30, Male, Female, Moms, Dad's and active athletes of all ages

Clothing

• Simply put I want people to say "whoa..."". When they use the product they say it and instantly buy almost every time. Unfortunately i can't have everyone get to have a free demo. So I need the packaging to convey this and make people feel like it's the party they want to be invited to
• Think Zeph Ox and Murex. Relates to a very wide ranging diverse audience
• Not to look stupid, Cartoony or childish. This is not a gimick, it is a great product at a fair price. People have no problem paying for something that works and the packaging needs to reflect the same

```html
<!DOCTYPE html>
<html lang="en">
<head>
<meta charset="utf-8">
<title>Brisa Nord Premium Cooling Towel – Tube Label</title>
<link rel="stylesheet" href="https://fonts.googleapis.com/css2?family=Roboto+Condensed:ital,wght@0,400;0,700;0,900;1,700&display=swap">
<style>
  :root {
    --page-bg: #eef2f6;
    --hot-red: #d8361f;
    --hot-red-dark: #b52514;
    --ice-blue: #2f6ea8;
    --ice-blue-deep: #23588c;
    --brand-blue: #1f63c6;
    --silver: #b9bec4;
    --silver-light: #dde1e5;
    --label-white: #fbfbfb;
    --pill-blue: #4da3e2;
    --text-white: #ffffff;
    --text-soft: #f4d9d3;
  }
  * { margin: 0; padding: 0; box-sizing: border-box; }
  html, body {
    width: 1200px;
    height: 1000px;
    overflow: hidden;
    background: var(--page-bg);
    font-family: "Roboto Condensed", Arial, sans-serif;
  }
  .canvas {
    position: relative;
    width: 1200px;
    height: 1000px;
  }
  .tube-label {
    position: absolute;
    left: 340px;
    top: 50px;
    width: 520px;
    height: 900px;
    border-radius: 10px;
    overflow: hidden;
    box-shadow: 0 6px 24px rgba(30, 50, 80, 0.18);
  }
  .tube-label__art {
    position: absolute;
    inset: 0;
    width: 520px;
    height: 900px;
  }
  .claim {
    position: absolute;
    left: 86px;
    top: 212px;
    color: var(--text-white);
  }
  .claim__word {
    font-weight: 900;
    font-size: 66px;
    line-height: 1;
    letter-spacing: 1px;
  }
  .claim__detail {
    margin-top: 6px;
    padding-left: 8px;
    font-weight: 400;
    font-size: 20px;
    line-height: 1.1;
    text-transform: uppercase;
  }
  .brand {
    position: absolute;
    left: 0;
    right: 0;
    top: 470px;
    text-align: center;
  }
  .brand__name {
    font-weight: 900;
    font-size: 58px;
    letter-spacing: 1px;
    color: var(--brand-blue);
    line-height: 1;
  }
  .brand__mark {
    display: block;
    width: 70px;
    height: 70px;
    margin: 24px auto 0;
    border-radius: 50%;
    background: var(--hot-red);
  }
  .product-tag {
    position: absolute;
    left: 70px;
    top: 800px;
    width: 320px;
    height: 42px;
    border-radius: 21px;
    background: var(--pill-blue);
    color: var(--text-white);
    font-style: italic;
    font-weight: 700;
    font-size: 24px;
    line-height: 42px;
    text-align: center;
  }
  .care-note {
    position: absolute;
    left: 96px;
    top: 852px;
    color: var(--text-soft);
    font-size: 20px;
    font-weight: 400;
  }
</style>
</head>
<body>
<main class="canvas">
  <section class="tube-label" aria-label="Brisa Nord cooling towel tube label">
    <svg class="tube-label__art" viewBox="0 0 520 900" aria-hidden="true">
      <defs>
        <linearGradient id="redFill" x1="0" y1="0" x2="1" y2="0">
          <stop offset="0" stop-color="var(--hot-red-dark)"/>
          <stop offset="0.45" stop-color="var(--hot-red)"/>
          <stop offset="1" stop-color="var(--hot-red-dark)"/>
        </linearGradient>
        <linearGradient id="blueFill" x1="0" y1="0" x2="1" y2="0">
          <stop offset="0" stop-color="var(--ice-blue-deep)"/>
          <stop offset="0.5" stop-color="var(--ice-blue)"/>
          <stop offset="1" stop-color="var(--ice-blue-deep)"/>
        </linearGradient>
      </defs>
      <rect class="band-white" x="0" y="0" width="520" height="900" fill="var(--label-white)"/>
      <rect class="band-top-red" x="0" y="0" width="520" height="200" fill="url(#redFill)"/>
      <path class="band-silver-upper" d="M0 190 H520 V300 Q300 330 0 490 Z" fill="var(--silver)"/>
      <path class="band-blue" d="M0 190 H520 V284 Q300 314 0 474 Z" fill="url(#blueFill)"/>
      <path class="band-silver-lower" d="M0 788 Q260 640 520 590 V900 H0 Z" fill="var(--silver-light)"/>
      <path class="band-bottom-red" d="M0 804 Q260 656 520 606 V900 H0 Z" fill="url(#redFill)"/>
    </svg>

    <div class="claim">
      <p class="claim__word">COOL</p>
      <p class="claim__detail">Long<br>Lasting</p>
    </div>

    <div class="brand">
      <p class="brand__name">BRISA NORD</p>
      <span class="brand__mark"></span>
    </div>

    <p class="product-tag">Instant Cooling Towel</p>
    <p class="care-note">Washable &amp; Reusable.</p>
  </section>
</main>
</body>
</html>
```